Contemporary Elegant Business Card Design for an International Trade Company in the Wine Industry

We need a new business card design for an international trade company in the wine and winemaking industry. The overall feel of the card should be contemporary, upscale, luxurious and elegant. It should communicate confidence and professionalism. The colors should complementary to our logo design (burgundy, gold, and black).
Inspiration: rich velvet tapestry
The card should include the following information:
Business: Brovenna Trading/Shipping, LLC.
Name: Marcus T. Hollenbrand
Title: CEO
Email: mark@brovennatrading.example
Phone: 555-294-6172
www.brovennatrading.example
Updates
Project Deadline Extended
Reason: We'd like the designers that we requested some additional designs from to still submit designs. Thank you!
Industry/Entity Type
Business
Contact Information for Business Card
Title: CEO
Phone: 555-294-6172
www.brovennatrading.example
Look and feel

```html
<!DOCTYPE html>
<html lang="en">
<head>
<meta charset="utf-8">
<title>Brovenna Trading/Shipping, LLC. – Business Card</title>
<link rel="stylesheet" href="https://fonts.googleapis.com/css2?family=Source+Sans+3:wght@400&display=swap">
<style>
  :root {
    --burgundy: #6f121a;
    --gold: #e2b452;
    --blush: #ecd6d9;
    --white: #f6eeee;
    --black: #000000;
    --edge: #2a0508;
  }
  html, body {
    margin: 0;
    padding: 0;
    width: 1200px;
    height: 686px;
    overflow: hidden;
    background: var(--black);
  }
  .card {
    position: relative;
    width: 1200px;
    height: 686px;
    background: var(--black);
    font-family: "Source Sans 3", "Myriad Pro", Arial, sans-serif;
  }
  .card-face {
    position: absolute;
    left: 0;
    top: 0;
    width: 1200px;
    height: 638px;
    background: var(--burgundy);
    box-shadow: inset 0 0 0 1px var(--edge);
  }
  .bottom-accent {
    position: absolute;
    left: 0;
    top: 0;
  }
  .brand-mark {
    position: absolute;
    left: 84px;
    top: 113px;
    width: 140px;
    height: 140px;
    border: 6px solid var(--gold);
    border-radius: 50%;
    box-sizing: border-box;
  }
  .brand-name {
    position: absolute;
    left: 328px;
    top: 112px;
    margin: 0;
    color: var(--gold);
    font-weight: 400;
    text-transform: uppercase;
    line-height: 1;
  }
  .brand-name .brand-primary {
    display: block;
    font-size: 96px;
    letter-spacing: 6px;
  }
  .brand-name .brand-secondary {
    display: block;
    margin-top: 8px;
    font-size: 33px;
    letter-spacing: 7px;
  }
  .person-name {
    position: absolute;
    left: 25px;
    top: 318px;
    margin: 0;
    font-size: 44px;
    font-weight: 400;
    color: var(--gold);
    line-height: 1;
  }
  .person-title {
    position: absolute;
    left: 78px;
    top: 372px;
    margin: 0;
    font-size: 28px;
    color: var(--white);
    line-height: 1;
  }
  .name-rule {
    position: absolute;
    left: 454px;
    top: 354px;
    width: 746px;
    height: 6px;
    background: var(--blush);
  }
  .contact-list {
    position: absolute;
    left: 705px;
    top: 398px;
    margin: 0;
    padding: 0;
    list-style: none;
  }
  .contact-item {
    display: flex;
    align-items: center;
    height: 52px;
    margin-bottom: 25px;
    color: var(--white);
    font-size: 30px;
  }
  .contact-item svg {
    width: 54px;
    height: 52px;
    flex: none;
    margin-right: 22px;
  }
</style>
</head>
<body>
<div class="card">
  <div class="card-face"></div>
  <svg class="bottom-accent" width="1200" height="686" viewBox="0 0 1200 686" aria-hidden="true">
    <polygon points="896,638 914,638 889,686 871,686" fill="var(--burgundy)"/>
  </svg>

  <div class="brand-mark" aria-hidden="true"></div>
  <h1 class="brand-name">
    <span class="brand-primary">Brovenna</span>
    <span class="brand-secondary">Trading/Shipping, LLC.</span>
  </h1>

  <p class="person-name">Marcus T. Hollenbrand</p>
  <p class="person-title">Chief Executive Officer</p>
  <div class="name-rule"></div>

  <ul class="contact-list">
    <li class="contact-item">
      <svg viewBox="0 0 54 52" aria-hidden="true">
        <rect x="1" y="10" width="52" height="34" fill="var(--gold)"/>
        <polyline points="2,12 27,31 52,12" fill="none" stroke="var(--burgundy)" stroke-width="3"/>
        <line x1="2" y1="43" x2="21" y2="27" stroke="var(--burgundy)" stroke-width="2.5"/>
        <line x1="52" y1="43" x2="33" y2="27" stroke="var(--burgundy)" stroke-width="2.5"/>
      </svg>
      <span>mark@brovennatrading.example</span>
    </li>
    <li class="contact-item">
      <svg viewBox="0 0 54 52" aria-hidden="true">
        <path d="M10 4 L19 4 L22 15 L16 20 C20 29 25 34 33 38 L38 32 L49 35 L49 44 C49 47 46 49 42 48 C22 44 8 30 5 10 C4 6 7 4 10 4 Z" fill="var(--gold)"/>
        <path d="M30 8 A15 15 0 0 1 45 23" fill="none" stroke="var(--gold)" stroke-width="3"/>
        <path d="M30 15 A8 8 0 0 1 38 23" fill="none" stroke="var(--gold)" stroke-width="3"/>
      </svg>
      <span>555-294-6172</span>
    </li>
    <li class="contact-item">
      <svg viewBox="0 0 54 52" aria-hidden="true">
        <circle cx="27" cy="26" r="23" fill="var(--gold)"/>
        <g fill="none" stroke="var(--burgundy)" stroke-width="2.5">
          <ellipse cx="27" cy="26" rx="10" ry="22"/>
          <line x1="27" y1="3" x2="27" y2="49"/>
          <line x1="4" y1="26" x2="50" y2="26"/>
          <line x1="8" y1="15" x2="46" y2="15"/>
          <line x1="8" y1="37" x2="46" y2="37"/>
        </g>
      </svg>
      <span>www.brovennatrading.example</span>
    </li>
  </ul>
</div>
</body>
</html>
```